Tactical Supply Company needing memorable business card design

Our tactical supply comapny is in need of a new business card design that will set us apart from the amateurs. We sell tactical gear ranging from backpacks and range bags to apparel and other gear. We are looking for a sharp design that incorporates our logo, website, and name. Our colors are white, red, and black, or any combination of the three, preferably red and black.
I have attached our logo with our name underneath but I have also edited that design with the logo incorporated next to the name (attached).

Target Market(s)

Law enforcement, military, tactical

Industry/Entity Type

Business

Contact Information for Business Card

Include www.fernhollowprovisions-demo.com

Colors
000000
ec1f27
ffffff

Requirements
Must have
• Our name, logo, and website. This is intended to be a memorable simple card, no name, address, email, or phone number info is necessary. Designs that do include this additional info will still be considered if they are absolutely spectacular.
Should not have
• A standard template design, I can create that in my own on Cardvellum. I am looking for a new, creative design that is completely unique to my company.

```html
<!DOCTYPE html>
<html lang="en">
<head>
<meta charset="utf-8">
<title>Fern Hollow Provisions – Business Card</title>
<link href="https://fonts.googleapis.com/css2?family=Roboto:wght@300;400;700&display=swap" rel="stylesheet">
<style>
  :root {
    --page-bg: #2a2624;
    --card-black: #0b0b0b;
    --card-plate: #1a1a1a;
    --brand-red: #ec1f27;
    --brand-white: #ffffff;
    --muted-white: #d9d9d9;
  }
  html, body {
    margin: 0;
    width: 1200px;
    height: 851px;
    overflow: hidden;
    background: var(--page-bg);
    font-family: "Roboto", Arial, sans-serif;
  }
  .business-card {
    position: absolute;
    left: 150px;
    top: 168px;
    width: 900px;
    height: 514px;
    background: var(--card-black);
    box-shadow: 0 18px 40px rgba(0,0,0,.55);
    overflow: hidden;
  }
  .plate-texture {
    position: absolute;
    inset: 0;
    background: radial-gradient(ellipse at 60% 30%, var(--card-plate), var(--card-black) 75%);
  }
  .card-content {
    position: absolute;
    inset: 0;
    display: flex;
    flex-direction: column;
    align-items: center;
    justify-content: center;
    text-align: center;
  }
  .brand-lockup {
    display: flex;
    align-items: center;
    gap: 14px;
    margin-bottom: 44px;
  }
  .brand-mark {
    width: 30px;
    height: 30px;
    background: var(--brand-red);
  }
  .brand-name {
    color: var(--brand-white);
    font-weight: 700;
    font-size: 44px;
    letter-spacing: 1px;
    text-transform: uppercase;
  }
  .holder-name {
    color: var(--muted-white);
    font-size: 24px;
    font-weight: 300;
    letter-spacing: 1px;
    margin-bottom: 18px;
  }
  .contact-line {
    color: var(--brand-red);
    font-size: 17px;
    font-weight: 400;
    letter-spacing: .5px;
    white-space: nowrap;
  }
</style>
</head>
<body>
  <div class="business-card">
    <div class="plate-texture" role="img" aria-label="Black diamond tread-plate texture across the card"></div>
    <div class="card-content">
      <div class="brand-lockup">
        <span class="brand-mark"></span>
        <span class="brand-name">Fern Hollow Provisions</span>
      </div>
      <div class="holder-name">Dana Merrow</div>
      <div class="contact-line">555 010 123 | dana.merrow@fernhollow-demo.com | www.fernhollowprovisions-demo.com</div>
    </div>
  </div>
</body>
</html>
```